Verindo Living- Hang tags for Modern Handmade Home Decor products

We need to design some hang tags to use for our products, we want double tags, meaning two tags that go together on one string, two different and coordinating sizes and shapes. We have a logo, what we need is the artwork for these two tags to take to print. One tag will have the logo on one side and company information on the other, the second tag will be for product information. For example, we specialize in handmade pieces from Latin America, on the product tag I want space to write the product info but also a line for what country it's from and what community created it. I'm attaching an image of the shapes of tags that I like, along with a copy of our logo. On the larger company tag I'd like our logo in the center and a color block stripe of the yellow color of our logo at the bottom, on the flip side there will just be text, sort of our company motto. On the narrower longer product info tag I'd like a small logo at the bottom end and space for product information to be written in by hand and on the flip side of this one lines for what country it's from, what community created it and care instructions, again, all information that we will write in by hand. Please let me know if you have questions.

Target Market(s)

Design savvy, house proud, well educated people who travel and appreciate art.

Font styles to use
Sans Serif

Requirements
Must have
• I want it to look graphic, sophisticated and modern. I want to be very legible and clean.
Nice to have
• Clarity, easy to read, and maybe a bit of whimsy or lightheartedness.
Should not have
• Nothing that feels "ethnic" or "crafty:, even though our products are handmade in Latin America they are contemporary and sophisticated, not stereotypical.

```html
<!DOCTYPE html>
<html lang="en">
<head>
<meta charset="utf-8">
<title>Verindo Living – Hang Tags</title>
<link href="https://fonts.googleapis.com/css2?family=Questrial&family=Montserrat:wght@400;600&display=swap" rel="stylesheet">
<style>
  :root {
    --backdrop: #f3f3f1;
    --card: #e8d388;
    --card-pale: #e9d48c;
    --brand-yellow: #ffd21a;
    --ink: #151515;
    --line: #2a2a2a;
    --art-red: #e03a30;
    --art-orange: #ec9a2c;
    --art-green: #2f9a6a;
    --art-olive: #7a7a48;
    --shadow: rgba(0,0,0,0.28);
  }
  * { box-sizing: border-box; margin: 0; padding: 0; }
  html, body { width: 1200px; height: 1000px; overflow: hidden; }
  body {
    background: var(--backdrop);
    position: relative;
    font-family: "Questrial", "Helvetica Neue", Arial, sans-serif;
    color: var(--ink);
  }

  /* Company tag */
  .company-tag {
    position: absolute;
    left: 110px; top: 176px;
    width: 430px; height: 632px;
    background: var(--brand-yellow);
    border-radius: 42px;
    box-shadow: 3px 5px 8px var(--shadow);
    overflow: hidden;
  }
  .company-tag__face {
    position: absolute;
    left: 8px; top: 8px; right: 8px; bottom: 78px;
    background: var(--card);
    border-radius: 36px 36px 0 0;
  }
  .company-tag__mark {
    position: absolute;
    left: 50%; top: 100px;
    width: 180px; height: 180px;
    margin-left: -90px;
    background: var(--brand-yellow);
    border-radius: 50%;
    box-shadow: 2px 3px 4px rgba(0,0,0,0.15);
  }
  .company-tag__band {
    position: absolute;
    left: 0; right: 0; top: 357px;
    height: 68px;
    background: var(--brand-yellow);
    display: flex; align-items: center; justify-content: center;
  }
  .brand-name {
    font-family: "Questrial", "Helvetica Neue", Arial, sans-serif;
    font-weight: 400;
    color: var(--ink);
    line-height: 1;
  }
  .company-tag__band .brand-name { font-size: 58px; letter-spacing: 1px; }
  .company-tag__rule {
    position: absolute;
    left: 32px; right: 32px; top: 430px;
    height: 3px;
    background: linear-gradient(90deg, transparent, var(--ink) 15%, var(--ink) 85%, transparent);
    border-radius: 50%;
  }
  .company-tag__url {
    position: absolute;
    left: 0; right: 0; top: 444px;
    text-align: center;
    font-family: "Montserrat", Arial, sans-serif;
    font-size: 13px;
    letter-spacing: 2.6px;
  }
  .company-tag__origin {
    position: absolute;
    left: 0; right: 0; bottom: 0;
    height: 78px;
    display: flex; align-items: center; justify-content: center;
    font-family: "Montserrat", Arial, sans-serif;
    font-weight: 600;
    font-size: 26px;
    letter-spacing: 4px;
  }

  /* Product tag */
  .product-tag {
    position: absolute;
    left: 740px; top: 86px;
    width: 345px; height: 822px;
    background: var(--card);
    border-radius: 26px;
    box-shadow: 3px 5px 8px var(--shadow);
  }
  .product-tag__eyelet {
    position: absolute;
    left: 156px; top: 18px;
    width: 30px; height: 30px;
    border-radius: 50%;
    border: 4px solid #c9c9c9;
    background: var(--backdrop);
    box-shadow: inset 0 0 2px rgba(0,0,0,0.4);
  }
  .product-tag__art {
    position: absolute;
    left: 18px; top: 96px;
    width: 300px; height: 510px;
    border-radius: 60% 40% 45% 55% / 40% 35% 65% 60%;
    background:
      radial-gradient(circle at 75% 12%, var(--art-green) 0 14%, transparent 26%),
      radial-gradient(circle at 55% 88%, var(--art-olive) 0 10%, transparent 22%),
      radial-gradient(circle at 30% 55%, var(--art-red) 0 25%, transparent 45%),
      linear-gradient(160deg, var(--art-orange), var(--art-red) 60%, var(--art-orange));
    opacity: 0.9;
  }
  .product-tag__name {
    position: absolute;
    left: 0; right: 0; top: 622px;
    text-align: center;
    font-size: 54px;
    letter-spacing: 1px;
  }
  .product-tag__lines {
    position: absolute;
    left: 40px; top: 714px;
    width: 272px;
  }
  .write-line {
    height: 2px;
    background: var(--line);
    margin-bottom: 25px;
  }
  .write-line--short { width: 200px; }
  .product-tag__mark {
    position: absolute;
    left: 268px; top: 748px;
    width: 36px; height: 36px;
    background: var(--brand-yellow);
    box-shadow: 1px 2px 3px rgba(0,0,0,0.2);
  }
</style>
</head>
<body>

  <section class="company-tag" aria-label="Company tag">
    <div class="company-tag__face">
      <div class="company-tag__mark"></div>
    </div>
    <div class="company-tag__band">
      <span class="brand-name">verindo</span>
    </div>
    <div class="company-tag__rule"></div>
    <p class="company-tag__url">www.verindoliving.com</p>
    <p class="company-tag__origin">MADE IN USA</p>
  </section>

  <section class="product-tag" aria-label="Product tag">
    <div class="product-tag__eyelet"></div>
    <div class="product-tag__art" role="img" aria-label="Decorative illustration of colourful teardrop and petal shapes in red, orange, yellow and green"></div>
    <p class="product-tag__name brand-name">verindo</p>
    <div class="product-tag__lines">
      <div class="write-line"></div>
      <div class="write-line write-line--short"></div>
      <div class="write-line write-line--short"></div>
      <div class="write-line write-line--short"></div>
    </div>
    <div class="product-tag__mark"></div>
  </section>

</body>
</html>
```